Post-ShelterLine Relief Shelters and Logistics Services

We need a brochure for a new company based in NE PA. We provide post-ShelterLine Relief shelters and accessories to non-profit organizations who participate in ShelterLine Relief. I'm starting with the brochure but ultimately we need brochures, flyers and business cards that match the look and feel of the brochure. I've included some designs that are horrific...but should provide some product information. Although the attached feature the shelter, what we really provide is a one-phone-call solution to housing and storage problems that volunteers frequently encounter at a post-disaster site. The design does not need to be a tri-fold...in fact, I would prefer a full color, bi-fold 11X17.

Target Market(s)

Non profit organizations that participate in post-ShelterLine Relief services.

Industry/Entity Type

It Company

Font styles to use
Serif

Requirements
Must have
• A clean professional look that conveys the message "Disaster Doesn't Call Ahead...But You Can!" Must be a larger than normal font as most of our clients are 50+. must have large full color photo's that we will provide. a look and feel that says "When you are done with your work-day, at a disaster site, you can be warm dry and comfortable, prepare a hot meal, and get a good nights sleep.
Nice to have
• I would like the cover to be enticing. I would like the back page to focus on the unit itself... The interior will focus on logistics( once under contract, the client can make one phone call and their unit shows up at the location of their choosing) and the 3 ownership options...buy, lease, or rent.
Should not have
• Appearance of a home-made design. hard to read. charts and statistics

```html
<!DOCTYPE html>
<html lang="en">
<head>
<meta charset="utf-8">
<title>ShelterLine Relief – Bi-fold Brochure</title>
<link href="https://fonts.googleapis.com/css2?family=Oswald:wght@400;600;700&family=Open+Sans:wght@400;600;700&family=Playfair+Display:ital,wght@1,700&display=swap" rel="stylesheet">
<style>
:root{
  --red:#d81e23;
  --deep-red:#8c1014;
  --ink:#151515;
  --charcoal:#2a2a2a;
  --paper:#ffffff;
  --grey:#6b6b6b;
  --stage:#e4e4e4;
}
*{box-sizing:border-box;margin:0;padding:0}
html,body{width:1200px;height:2200px;overflow:hidden}
body{background:var(--stage);font-family:"Open Sans",Arial,sans-serif;color:var(--ink);position:relative}
.spread{position:absolute;left:40px;width:1120px;height:724px;display:flex;box-shadow:0 8px 24px rgba(0,0,0,.18)}
.spread--outside{top:320px}
.spread--inside{top:1140px}
.panel{position:relative;width:560px;height:724px;overflow:hidden;background:var(--paper)}
.panel--dark{background:var(--ink)}
.panel svg.bg{position:absolute;inset:0;width:100%;height:100%}
.abs{position:absolute}
.photo{position:absolute}
.head{font-family:"Oswald",Arial,sans-serif;font-weight:700;text-transform:uppercase;line-height:1.12}
.small{font-size:10.5px;line-height:1.45;color:var(--grey)}
/* back panel */
.back-banner{left:78px;top:42px;color:#fff;font-size:19px}
.tick-list{left:36px;top:140px;list-style:none;width:250px}
.tick-list li{position:relative;padding-left:20px;font-size:11.5px;color:var(--charcoal);margin-bottom:9px}
.tick-list li::before{content:"";position:absolute;left:2px;top:3px;width:8px;height:4px;border-left:2px solid var(--red);border-bottom:2px solid var(--red);transform:rotate(-45deg)}
.back-para{left:300px;top:212px;width:230px}
.motto{font-family:"Oswald",Arial,sans-serif;font-weight:700;font-style:italic;color:var(--red);font-size:18px;letter-spacing:.5px}
.motto-block{left:36px;width:240px}
.back-contact{left:36px;top:552px}
.back-contact .phone{font-family:"Oswald",Arial,sans-serif;font-weight:700;color:var(--red);font-size:22px;display:flex;align-items:center;gap:8px}
.back-contact .web{font-size:12px;color:var(--charcoal);margin-top:4px;font-weight:600}
/* cover */
.cover-question{right:40px;top:50px;font-family:"Playfair Display",Georgia,serif;font-style:italic;font-weight:700;color:#fff;font-size:50px;line-height:1.05;text-align:right;text-shadow:0 2px 8px rgba(0,0,0,.5)}
.cover-tag{left:60px;top:500px;text-align:left}
.cover-brand{display:flex;align-items:center;gap:8px;font-family:"Oswald",Arial,sans-serif;font-weight:600;font-size:15px;color:var(--charcoal);text-transform:uppercase;letter-spacing:1px}
.cover-brand .sq{width:14px;height:14px;background:var(--red)}
.cover-tag .line1{font-family:"Oswald",Arial,sans-serif;font-weight:600;color:var(--deep-red);font-size:24px;text-transform:uppercase;margin-top:14px}
.cover-tag .line2{font-family:"Oswald",Arial,sans-serif;font-weight:700;color:var(--red);font-size:62px;text-transform:uppercase;line-height:1}
/* inside left */
.inside-head{left:40px;top:44px;font-size:30px;color:#fff}
.inside-head .hl{color:var(--red)}
/* inside right */
.call-block{left:36px;top:60px}
.call-block .label{font-family:"Oswald",Arial,sans-serif;font-weight:600;font-size:16px;color:var(--charcoal);text-transform:uppercase}
.call-block .phone{font-family:"Oswald",Arial,sans-serif;font-weight:700;font-size:28px;color:var(--red)}
.option{position:absolute;left:30px;width:200px;display:flex;gap:10px;align-items:flex-start}
.option .dot{flex:none;width:44px;height:44px;border-radius:50%;background:var(--red);color:#fff;font-family:"Oswald",Arial,sans-serif;font-weight:700;font-size:12px;display:flex;align-items:center;justify-content:center;box-shadow:0 0 0 3px #fff,0 0 0 4px var(--red)}
.option h3{font-family:"Oswald",Arial,sans-serif;font-size:13px;color:var(--red);text-transform:uppercase;margin-bottom:2px}
.inside-web{left:0;right:0;bottom:34px;text-align:center;font-family:"Oswald",Arial,sans-serif;font-size:16px;letter-spacing:1px;color:var(--charcoal)}
.brand-mark{display:flex;align-items:center;gap:10px}
.brand-mark .sq{width:14px;height:14px;background:var(--red)}
</style>
</head>
<body>

<section class="spread spread--outside">
  <article class="panel panel--back">
    <svg class="bg" viewBox="0 0 560 724" aria-hidden="true">
      <polygon points="0,30 345,30 315,112 0,112" fill="#d81e23"/>
      <polygon points="0,30 60,30 60,112 0,112" fill="#8c1014"/>
      <polygon points="0,600 330,724 0,724" fill="#151515"/>
      <polygon points="0,575 60,597 0,620" fill="#d81e23"/>
      <polygon points="260,724 340,724 110,640 80,652" fill="#d81e23"/>
      <polygon points="560,0 560,90 470,0" fill="#151515"/>
      <polygon points="530,0 560,0 560,30" fill="#d81e23"/>
      <rect x="22" y="62" width="16" height="16" fill="#fff"/>
    </svg>
    <h2 class="abs head back-banner">Give one phone call and<br>have a shelter delivered<br>to the post-disaster site</h2>
    <div class="photo" role="img" aria-label="Photo of a furnished shelter interior with beds" style="left:360px;top:40px;width:180px;height:150px;background:linear-gradient(135deg,#f4f2ee,#b9b4ab)"></div>
    <ul class="abs tick-list">
      <li>Warm, dry private sleeping space</li>
      <li>Kitchen ready for hot meals</li>
      <li>Secure storage for your supplies</li>
      <li>Delivered where you need it</li>
      <li>Set up fast by our crew</li>
    </ul>
    <p class="abs small back-para">After a long work day at a disaster site, your volunteers deserve a clean, comfortable place to rest. Our units arrive ready to use.</p>
    <div class="abs motto-block" style="top:330px">
      <p class="motto">* BE EFFECTIVE *</p>
      <p class="small">Keep your teams rested, fed and working well.</p>
    </div>
    <div class="abs motto-block" style="top:405px">
      <p class="motto">* BE PREPARED *</p>
      <p class="small">Secure your shelter before the next disaster strikes.</p>
    </div>
    <div class="photo" role="img" aria-label="Photo of a white portable shelter unit" style="left:300px;top:340px;width:240px;height:170px;background:linear-gradient(160deg,#fbfbfb,#c9d2da)"></div>
    <div class="abs back-contact">
      <div class="phone">
        <svg width="18" height="18" viewBox="0 0 24 24" aria-hidden="true"><path fill="#d81e23" d="M6.6 10.8a15 15 0 0 0 6.6 6.6l2.2-2.2a1 1 0 0 1 1-.25 11.4 11.4 0 0 0 3.6.57 1 1 0 0 1 1 1V20a1 1 0 0 1-1 1A17 17 0 0 1 3 4a1 1 0 0 1 1-1h3.5a1 1 0 0 1 1 1c0 1.25.2 2.45.57 3.57a1 1 0 0 1-.25 1z"/></svg>
        (570) 555-0148
      </div>
      <div class="web">www.shelterlinerelief.com</div>
    </div>
  </article>

  <article class="panel panel--cover">
    <svg class="bg" viewBox="0 0 560 724" role="img" aria-label="Photo of a road under a dark stormy sky">
      <defs>
        <linearGradient id="storm" x1="0" y1="0" x2="0" y2="1">
          <stop offset="0" stop-color="#2b2f36"/>
          <stop offset=".55" stop-color="#6e6a66"/>
          <stop offset="1" stop-color="#3a3632"/>
        </linearGradient>
      </defs>
      <polygon points="0,0 560,0 560,360 0,470" fill="url(#storm)"/>
      <polygon points="0,470 560,360 560,385 0,495" fill="#d81e23"/>
      <polygon points="0,495 560,385 560,398 0,508" fill="#151515"/>
      <polygon points="560,724 560,590 330,724" fill="#151515"/>
      <polygon points="560,560 560,590 330,724 290,724" fill="#d81e23"/>
    </svg>
    <h1 class="abs cover-question">Are You<br>Ready?</h1>
    <div class="abs cover-tag">
      <p class="cover-brand"><span class="sq"></span>ShelterLine Relief</p>
      <p class="line1">Disaster doesn't call ahead...</p>
      <p class="line2">But you can!</p>
    </div>
  </article>
</section>

<section class="spread spread--inside">
  <article class="panel panel--dark">
    <svg class="bg" viewBox="0 0 560 724" aria-hidden="true">
      <polygon points="330,0 560,0 560,724 520,724" fill="#8c1014"/>
      <polygon points="400,0 430,0 560,520 560,640" fill="#d81e23"/>
      <polygon points="0,650 560,560 560,580 0,680" fill="#d81e23"/>
    </svg>
    <h2 class="abs head inside-head">Give one phone call and<br><span class="hl">to the post-disaster site</span><br>have a shelter delivered</h2>
    <div class="photo" role="img" aria-label="Image of the earth seen from space during a disaster" style="left:40px;top:190px;width:230px;height:220px;background:linear-gradient(180deg,#3a2a26,#6a2418)"></div>
    <div class="photo" role="img" aria-label="Photo of a white portable shelter unit" style="left:110px;top:430px;width:330px;height:150px;background:linear-gradient(160deg,#ffffff,#c6cfd8)"></div>
  </article>

  <article class="panel panel--inside-right">
    <svg class="bg" viewBox="0 0 560 724" aria-hidden="true">
      <polygon points="0,0 22,0 0,40" fill="#d81e23"/>
      <polygon points="560,630 560,724 400,724" fill="#151515"/>
      <polygon points="560,600 560,630 400,724 360,724" fill="#d81e23"/>
    </svg>
    <div class="photo" role="img" aria-label="Photos of a shelter interior with bed and kitchen" style="left:360px;top:20px;width:180px;height:190px;background:linear-gradient(135deg,#f1ede6,#a9a299)"></div>
    <div class="photo" role="img" aria-label="Photo of storm debris at a disaster site" style="left:240px;top:225px;width:300px;height:200px;clip-path:polygon(20% 0,100% 0,100% 100%,0 100%);background:linear-gradient(150deg,#8fa2b0,#6f6455 60%,#3c342c)"></div>
    <div class="abs call-block">
      <p class="label">Call us on order</p>
      <p class="phone">(570) 555-0148</p>
    </div>
    <div class="option" style="top:170px">
      <span class="dot">BUY</span>
      <div><h3>Buy your unit</h3><p class="small">Own a shelter, stored and ready for any call.</p></div>
    </div>
    <div class="option" style="top:270px">
      <span class="dot">LEASE</span>
      <div><h3>Lease your unit</h3><p class="small">Flexible terms with delivery to any site.</p></div>
    </div>
    <div class="option" style="top:370px">
      <span class="dot">RENT</span>
      <div><h3>Rent your unit</h3><p class="small">Short stays for a single relief mission.</p></div>
    </div>
    <div class="abs inside-web brand-mark" style="justify-content:center">
      <span class="sq"></span>www.shelterlinerelief.com
    </div>
  </article>
</section>

</body>
</html>
```